Website design for online service business

The company provides the following services:
1 - consultancy services on existing products (like tallydesk and brisk 354)
2 - Coaching services - Coach someone on services like using/developing features with existing products, or teach how to be more productive, or improve their business using automation, etc
3 - Training
- Online training on demand on existing products via vokra (like in Tallydesk and brisk 365)
- Online courses through videos lessons and scripts by offering information products where people will need to register and pay in advance to access the online course. (productivity courses for example)

- The goal is for clients to book time with me for one of those areas without too many clicks.
- Clients will be able to Book time using an integration (it would be good to have the layout integrated with the site.) with this https://planner.brisk-suite.example/owa/calendar/BrightKelpStudio1@brightkelpstudio.bookhub.example/bookings/

- there will be areas for which i whish to build a VIP mailing list. It's referenced on the wireframes

References:
https://www.lanternfieldnotes.example/about/about-dorvan/
https://www.pebblecompass.example/
https://tallydeskguide.example/

Target Market(s)

- Small businesses
- Freelancers

Industry/Entity Type

Business

Number of Pages Required

5+ page

Font styles to use
Sans Serif

Colors

Designer to choose colors to be used in the design.

Requirements
Must have
• Must have the design optimized to the less clicks possible to achieve any action
• The colors of the site should follow the logo (provided in attach)
• It should use other color that belong to the same pallet of colors
• Should contain colors that incentivizes people to click and book something
• Images and backgrounds should be made available
• All images sizes and colors should be provided to be able to develop the site according to the design
Nice to have
• The bookings for the time should be integrated within the design. If not possible a redirection to it can work as well.
Should not have
• Links to social media
• Pop-ups
• Intrusive navigations (like navigation bares on the left or right hand side)
• Should not be a template used by many people

```html
<!DOCTYPE html>
<html lang="en">
<head>
<meta charset="utf-8">
<title>Bright Kelp Studio</title>
<link href="https://fonts.googleapis.com/css2?family=Lato:wght@400;700&display=swap" rel="stylesheet">
<style>
:root{
  --orange:#f28a1c;
  --orange-deep:#ee6f0f;
  --blue:#0f5b92;
  --blue-deep:#0a4574;
  --navy:#1b3550;
  --grey:#e8e8e8;
  --ink:#222;
  --muted:#444;
  --white:#fff;
}
*{margin:0;padding:0;box-sizing:border-box}
html,body{width:1200px;height:2941px;overflow:hidden}
body{font-family:'Lato',sans-serif;color:var(--ink);background:var(--white);position:relative}
.nav{position:absolute;top:0;left:0;width:1200px;height:57px;background:var(--orange);display:flex;justify-content:center}
.nav ul{list-style:none;display:flex;height:57px}
.nav li{color:var(--white);font-size:16px;font-weight:700;text-transform:uppercase;padding:0 23px;display:flex;align-items:center;border-right:1px solid rgba(255,255,255,.35)}
.nav li:last-child{border-right:none}
.nav li.active{background:var(--blue);padding:0 30px}
.hero{position:absolute;top:57px;left:0;width:1200px;height:550px;background:linear-gradient(120deg,#2f7fae 0%,#4b9ac4 45%,#3a7ba6 70%,#2a6793 100%)}
.hero-arrow{position:absolute;top:240px;width:50px;height:50px}
.brand{position:absolute;top:180px;left:0;width:1200px;text-align:center;color:var(--white)}
.brand-name{font-size:62px;font-weight:400;letter-spacing:8px;text-transform:uppercase;line-height:1}
.brand-sub{font-size:22px;letter-spacing:14px;margin-top:14px}
.tagline{position:absolute;top:345px;left:0;width:1200px;text-align:center;color:var(--white);font-size:39px}
.band{position:absolute;left:0;width:1200px;height:88px;display:flex;align-items:center;justify-content:center;color:var(--white);font-size:31px}
.band-blue{background:linear-gradient(#1266a3,var(--blue-deep))}
.band-orange{background:linear-gradient(var(--orange-deep),var(--orange))}
.pointer{position:absolute;left:50%;bottom:-18px;margin-left:-30px;width:60px;height:18px}
.services{position:absolute;top:762px;left:-10px;width:1200px;display:flex;justify-content:center;gap:58px}
.service{width:285px;text-align:center}
.service-art{margin:0 auto}
.art-teach{width:216px;height:228px;background:linear-gradient(100deg,#e9e9ea 0%,#f0b08a 28%,#d8d8da 45%,#2e3440 62%,#3a404c 78%,#e4e4e4 100%)}
.art-rocket{width:186px;height:206px;margin-top:8px;background:radial-gradient(ellipse at 40% 62%,#3d4e9e 0%,#5a6fc0 22%,#f28a1c 48%,#f6b24a 66%,#fde3bf 86%,#fff 100%)}
.art-desk{width:246px;height:222px;background:linear-gradient(100deg,#f4f4f4 0%,#d63a2a 18%,#b9bcc2 38%,#2b2f3a 55%,#e0403a 72%,#9aa0a8 90%,#f2f2f2 100%)}
.service h3{font-size:27px;font-weight:400;margin-top:36px}
.service p{font-size:14px;line-height:20px;color:var(--muted);margin:10px auto 0;width:262px}
.btn{display:inline-block;background:var(--orange);color:var(--white);border-radius:22px;font-size:17px;font-weight:700;padding:11px 0;width:138px;margin-top:16px}
.why{position:absolute;top:1373px;left:0;width:1200px;height:472px;background:var(--grey)}
.card{position:absolute;top:57px;left:118px;width:959px;height:347px;background:var(--white);box-shadow:0 1px 5px rgba(0,0,0,.25);display:flex}
.card-photo{width:479px;height:347px;background:radial-gradient(ellipse 30% 42% at 48% 42%,#d7a58c 0%,#c08d76 55%,transparent 100%),linear-gradient(180deg,transparent 55%,#262a30 85%),linear-gradient(90deg,#5d6f45 0%,#8a9370 30%,#9c978e 55%,#6e6058 80%,#8b8880 100%)}
.card-body{flex:1;padding:38px 22px 0 36px;font-size:14px;line-height:21px;color:var(--muted)}
.card-body p+p{margin-top:16px}
.read-more{position:absolute;right:27px;bottom:30px;color:var(--blue);font-size:16px}
.questions{position:absolute;top:1980px;left:0;width:1200px;text-align:center;font-size:17px;color:var(--ink)}
.questions .lead{margin-bottom:55px}
.questions p.line{height:37.3px}
.cta{position:absolute;top:2455px;left:0;width:1200px;height:405px;background:linear-gradient(135deg,#2c4360,var(--navy) 50%,#243a55)}
.cta-box{position:absolute;border:1px solid rgba(255,255,255,.85);color:var(--white);text-align:center}
.cta-title{top:60px;left:500px;width:208px;height:44px;line-height:42px;font-size:21px}
.cta-text{top:118px;left:230px;width:748px;height:77px;padding-top:14px;font-size:17px;line-height:23px}
.cta-note{position:absolute;top:214px;left:0;width:1200px;text-align:center;color:var(--white);font-size:16px}
.book{position:absolute;top:268px;left:487px;width:226px;height:55px;border-radius:28px;background:var(--orange);color:var(--white);font-size:22px;display:flex;align-items:center;justify-content:center}
.footer{position:absolute;top:2860px;left:0;width:1200px;height:81px;color:#555;font-size:15px}
.copy{position:absolute;left:135px;top:28px}
.social{position:absolute;left:760px;top:28px;display:flex;gap:18px;font-size:14px}
.blog{position:absolute;left:1025px;top:26px}
</style>
</head>
<body>
<nav class="nav">
  <ul>
    <li class="active">Home</li><li>About us</li><li>Our Services</li><li>Teaching</li><li>FAQ</li><li>Testimonial</li><li>Contact us</li>
  </ul>
</nav>

<header class="hero" role="img" aria-label="Photo of a team working together at laptops, tinted blue">
  <svg class="hero-arrow" style="left:91px" viewBox="0 0 50 50"><circle cx="25" cy="25" r="23" fill="none" stroke="#fff" stroke-width="2"/><path d="M29 15 L19 25 L29 35" fill="none" stroke="#fff" stroke-width="3"/></svg>
  <svg class="hero-arrow" style="left:1077px" viewBox="0 0 50 50"><circle cx="25" cy="25" r="23" fill="none" stroke="#fff" stroke-width="2"/><path d="M21 15 L31 25 L21 35" fill="none" stroke="#fff" stroke-width="3"/></svg>
  <div class="brand">
    <div class="brand-name">Bright Kelp</div>
    <div class="brand-sub">STUDIO</div>
  </div>
  <div class="tagline">“..Because ideas are a million”</div>
</header>

<section class="band band-blue" style="top:607px">How Can I help you with your ideas?
  <svg class="pointer" viewBox="0 0 60 18"><path d="M0 0 H60 L30 18Z" fill="#0a4574"/></svg>
</section>

<section class="services">
  <div class="service">
    <div class="service-art art-teach" role="img" aria-label="Illustration of a businessman presenting an orange chart on a board"></div>
    <h3>I will Teach you</h3>
    <p>ullamcorper est eget tempor cursus neque mi consectetuer mi a ultricies massa est sed nisl Class aptent taciti sociosqu ad litora torquent per conubia nostra per</p>
    <span class="btn">Teach Me!</span>
  </div>
  <div class="service">
    <div class="service-art art-rocket" role="img" aria-label="Illustration of a blue rocket wrapped in orange flames"></div>
    <h3>We do it Together</h3>
    <p>ullamcorper est eget tempor cursus neque mi consectetuer mi a ultricies massa est sed nisl Class aptent taciti sociosqu ad litora torquent per conubia nostra per</p>
    <span class="btn">Let’s do it!</span>
  </div>
  <div class="service">
    <div class="service-art art-desk" role="img" aria-label="Illustration of a woman working at a desk with a laptop and red lamp"></div>
    <h3>I’ll do it for you</h3>
    <p>ullamcorper est eget tempor cursus neque mi consectetuer mi a ultricies massa est sed nisl Class aptent taciti sociosqu ad litora torquent per conubia nostra per</p>
    <span class="btn">Do It for me!</span>
  </div>
</section>

<section class="band band-blue" style="top:1285px">Why Should you hire my Services
  <svg class="pointer" viewBox="0 0 60 18"><path d="M0 0 H60 L30 18Z" fill="#0a4574"/></svg>
</section>

<section class="why">
  <div class="card">
    <div class="card-photo" role="img" aria-label="Portrait photo of the consultant in a dark jacket on a tree-lined street"></div>
    <div class="card-body">
      <p>Fusce ultricies orci ac feugiat suscipit leo massa sodales velit et scelerisque mi tortor at ipsum cligula augue bibendum accumsan vestibulum ut commodo a mi Morbi ornare gravida elit Integer congue augue et malesuada iaculis ipsum dui aliquet felis at cursus magna nisl nec elit Praesent elementum elit at tellus nec ultricies sit amet porttitor mattis enim In massa libero interdum nec interdum vel blandit sed nulla In ullamcorper est eget tempor cursus neque mi</p>
      <p>consectetuer mi a ultricies massa est sed nisl Class aptent taciti sociosqu ad litora torquent per conubia nostra per inceptos hymenaeos Proin nulla arcu nonummy luctus dictum</p>
    </div>
    <span class="read-more">Read More</span>
  </div>
</section>

<section class="band band-orange" style="top:1845px">Do you have any Questions?
  <svg class="pointer" viewBox="0 0 60 18"><path d="M0 0 H60 L30 18Z" fill="#f28a1c"/></svg>
</section>

<section class="questions">
  <p class="lead">It's ok if you have questions. We haven't worked together or met each other so how do you now if:</p>
  <p class="line">We can work together?</p>
  <p class="line">or</p>
  <p class="line">understand each other</p>
  <p class="line">or</p>
  <p class="line">(did i say work together?)</p>
  <p class="line">event if</p>
  <p class="line">I have the experience you are looking for?</p>
</section>

<section class="band band-blue" style="top:2366px">Don’t worry about anything</section>

<section class="cta" role="img" aria-label="Dark blue tinted photo of people meeting over coffee">
  <div class="cta-box cta-title">I'm here for you!</div>
  <div class="cta-box cta-text">Use the button below to book a time slot where we can have a chat about what you need<br>help with and we will take it from there</div>
  <p class="cta-note">With coffee included of course!</p>
  <span class="book">Book me</span>
</section>

<footer class="footer">
  <span class="copy">© 2018 Company Name&nbsp; All right reserved</span>
  <span class="social"><span>Kestrel</span><span>Fernbook</span><span>Linkwell</span><span>Orbitly</span></span>
  <span class="blog">Blog</span>
</footer>
</body>
</html>
```